We need a logo for our business which is a dental clinic (i.e. dentistry).
We would lilke designs using the colour blue, green and black incorporating the words Corvasta Dental, possibly a smile or a tooth image can be considered for incorporation in the logo.

Industry/Entity Type

Dental

```html
<!DOCTYPE html>
<html lang="en">
<head>
<meta charset="utf-8">
<title>Corvasta Dental – Business Card</title>
<link rel="stylesheet" href="https://fonts.googleapis.com/css2?family=Michroma&family=Open+Sans:wght@400;600&display=swap">
<style>
  :root {
    --page-bg: #eef1f4;
    --blue-deep: #1a78c8;
    --blue-mid: #2d9ade;
    --blue-light: #45c0ee;
    --accent-blue: #1f8fd6;
    --accent-green: #8cc63f;
    --text-grey: #8a8f94;
    --rule-grey: #c9cdd1;
    --white: #ffffff;
  }
  * { box-sizing: border-box; margin: 0; padding: 0; }
  html, body { width: 1200px; height: 855px; overflow: hidden; }
  body {
    background: var(--page-bg);
    font-family: "Open Sans", Arial, sans-serif;
    position: relative;
  }
  .card {
    position: absolute;
    width: 500px;
    height: 290px;
    border-radius: 30px;
    overflow: hidden;
    box-shadow: 0 14px 30px rgba(0,0,0,0.18);
  }

  /* Front */
  .card-front {
    left: 70px; top: 200px;
    background: radial-gradient(ellipse at 45% 50%, var(--blue-light) 0%, var(--blue-mid) 45%, var(--blue-deep) 100%);
  }
  .card-front .wordmark {
    position: absolute;
    left: 50px; top: 118px;
    font-family: "Michroma", sans-serif;
    color: var(--white);
    font-size: 30px;
    letter-spacing: 1px;
    line-height: 1;
  }
  .card-front .wordmark small {
    display: block;
    font-size: 13px;
    letter-spacing: 12px;
    margin-top: 8px;
    text-align: right;
  }
  .slogan-band {
    position: absolute;
    right: 46px; top: 0; bottom: 0;
    display: flex;
    flex-direction: column;
    align-items: center;
    gap: 12px;
  }
  .slogan-band .rule { width: 6px; background: var(--white); }
  .slogan-band .rule-top { height: 70px; }
  .slogan-band .rule-bottom { flex: 1; }
  .slogan {
    writing-mode: vertical-rl;
    transform: rotate(180deg);
    font-family: "Michroma", sans-serif;
    color: var(--white);
    font-size: 12px;
    letter-spacing: 1px;
  }

  /* Back */
  .card-back {
    left: 630px; top: 200px;
    background: var(--white);
  }
  .back-logo {
    position: absolute;
    left: 34px; top: 36px;
    font-family: "Michroma", sans-serif;
    color: var(--accent-blue);
    font-size: 19px;
    line-height: 1;
  }
  .back-logo small {
    display: block;
    font-size: 9px;
    letter-spacing: 8px;
    margin-top: 6px;
    text-align: right;
  }
  .address {
    position: absolute;
    left: 34px; top: 98px;
    color: var(--text-grey);
    font-size: 12px;
    line-height: 1.5;
  }
  .divider {
    position: absolute;
    left: 230px; top: 36px;
    width: 1px; height: 150px;
    background: var(--rule-grey);
  }
  .person {
    position: absolute;
    left: 250px; top: 36px;
  }
  .person .name {
    font-family: "Michroma", sans-serif;
    color: var(--accent-blue);
    font-size: 17px;
    letter-spacing: 0.5px;
  }
  .person .title {
    color: var(--text-grey);
    font-size: 12px;
    margin-top: 4px;
  }
  .contacts {
    list-style: none;
    margin-top: 18px;
    color: var(--text-grey);
    font-size: 12px;
    line-height: 1.7;
  }
  .contacts li { display: flex; align-items: center; gap: 7px; }
  .contacts svg { width: 12px; height: 12px; flex: none; }
  .appointment {
    position: absolute;
    left: 0; right: 0; bottom: 30px;
    display: flex;
    align-items: flex-end;
    gap: 10px;
    padding-right: 0;
  }
  .appointment .bar { width: 30px; height: 6px; background: var(--blue-light); align-self: center; }
  .appointment .bar-end { width: 60px; background: var(--accent-blue); }
  .appointment .label {
    font-family: "Michroma", sans-serif;
    font-size: 8px;
    color: var(--text-grey);
  }
  .appointment .line { flex: 1; height: 1px; background: var(--rule-grey); margin-bottom: 3px; }

  /* Standalone wordmark */
  .wordmark-standalone {
    position: absolute;
    left: 0; right: 0; top: 640px;
    text-align: center;
    font-family: "Michroma", sans-serif;
    color: var(--accent-blue);
    font-size: 34px;
    line-height: 1;
  }
  .wordmark-standalone small {
    display: block;
    font-size: 14px;
    letter-spacing: 14px;
    margin-top: 8px;
    padding-left: 150px;
  }
</style>
</head>
<body>
  <section class="card card-front" aria-label="Business card front">
    <div class="wordmark">CORVASTA<small>DENTAL</small></div>
    <div class="slogan-band">
      <span class="rule rule-top"></span>
      <span class="slogan">YOUR SLOGAN HERE</span>
      <span class="rule rule-bottom"></span>
    </div>
  </section>

  <section class="card card-back" aria-label="Business card back">
    <div class="back-logo">CORVASTA<small>DENTAL</small></div>
    <p class="address">Your Address Here<br>City, State, Country</p>
    <span class="divider"></span>
    <div class="person">
      <p class="name">YOUR NAME HERE</p>
      <p class="title">Title and Qualifications</p>
      <ul class="contacts">
        <li><svg viewBox="0 0 12 12"><circle cx="6" cy="6" r="6" fill="#8cc63f"/><path d="M4 3.2l1 1.6-.6.7c.4.8 1 1.4 1.9 1.9l.7-.6 1.6 1-.5 1.2C5.6 9 3 6.4 2.8 4z" fill="#fff"/></svg>555-014-2287</li>
        <li><svg viewBox="0 0 12 12"><circle cx="6" cy="6" r="6" fill="#8cc63f"/><path d="M4 3.2l1 1.6-.6.7c.4.8 1 1.4 1.9 1.9l.7-.6 1.6 1-.5 1.2C5.6 9 3 6.4 2.8 4z" fill="#fff"/></svg>555-014-2290</li>
        <li><svg viewBox="0 0 12 12"><circle cx="6" cy="6" r="6" fill="#8cc63f"/><rect x="3" y="4" width="6" height="4.2" fill="none" stroke="#fff" stroke-width="0.9"/><path d="M3 4l3 2.3L9 4" fill="none" stroke="#fff" stroke-width="0.9"/></svg>youremail@here.com</li>
      </ul>
    </div>
    <div class="appointment">
      <span class="bar"></span>
      <span class="label">DATE</span><span class="line"></span>
      <span class="label">TIME</span><span class="line"></span>
      <span class="label">AM/PM</span>
      <span class="bar bar-end"></span>
    </div>
  </section>

  <div class="wordmark-standalone">CORVASTA<small>DENTAL</small></div>
</body>
</html>
```